Nutrition-Cooking Website

Hello!
I am in a need of a lovely looking website for my new nutrition practice. I am looking for something sleek, sophisticated, professional yet also welcoming.

Here is a current layout which can be tweaked or overhauled. I feel like the website is not quite what I want so thats why I need your help!!
http://tolvanfolio.example/RENATA-OSSLER-concept-15/

Two websites I like are: (layout similar to www.marquetta.example) or http://www.pernillavostraken.example

Here are the tabs for the website:
About Registered Dietitian Healthy Recipes Philanthropy Shop Features Contact Blog

Features for the Home page include:
Slideshow with 3 rotating updates (like www.marquetta.example)
Video Box (like www.marquetta.example)
Recent Recipes (like http://harrowfield7731.example)
Recent Posts (like http://harrowfield7731.example)
Food Knowledge Box- quick tidbits on laws on food (like www.marquetta.example- she has food wisdom)
Tried and True Benefits of Mediterranean Cuisine (like www.marquetta.example)
Picture of me with brief quote/bio (like www.bettinoruval.example)
Social media buttons

Color Scheme:
• I like the white with gold embroidery or the pretty bluish/purplish in the first pic would be awesome with the slight pink undertones (http://glossedtwirl.example/2012/10/quorvel-marigelle-collection-by-tansley/)
• Also like this goldish background- exotic/sophisticated- http://www.thewhirlingcook.example/Home.html
• Also like the rustic goldish look in the background like this-
ohttp://img.prentlo.example/vexomarks_rsvp_vintage_rustic_gold_swirls_invitation-p161658028764768924bebn6_400.jpg
o http://img.prentlo.example/vexomarks_ornamental_rustic_gold_swirls_invitation-p161776340110432961bvddb_400.jpg
• maybe can have the vines as grapes/olives
OPEN TO ALL DIFFERENT COLORS SCHEMES- whatever looks, clean, sophisticated and professional

Logo:
• Attached is the logo

Budget is flexible. If you think you can improve the website- please do so :)

Target Market(s)

health conscious individuals of all ages

Industry/Entity Type

Embroidery

Requirements
Must have
• clean and sharp look
professional looking
Should not have
• too much busyness

```html
<!DOCTYPE html>
<html lang="en">
<head>
<meta charset="utf-8">
<title>Renata Ossler RD</title>
<link href="https://fonts.googleapis.com/css2?family=Cinzel:wght@400;700&family=Open+Sans:wght@300;400&display=swap" rel="stylesheet">
<style>
:root{
  --gold:#c9a959;
  --gold-light:#e6c56a;
  --gold-dark:#b08d3e;
  --grey-band:#7d7d7d;
  --page:#efefef;
  --ink:#222;
  --muted:#8a7d70;
  --panel:#f8f8f8;
  --tweet-bg:#f8f5e3;
}
*{box-sizing:border-box;margin:0;padding:0}
html,body{width:1032px;height:1200px;overflow:hidden}
body{position:relative;background:var(--page);font-family:Arial,Helvetica,sans-serif;color:var(--ink)}
.abs{position:absolute}
.header{left:0;top:0;width:1032px;height:121px;background:#fff}
.brand{left:101px;top:30px;font-family:'Cinzel',serif;font-size:33px;letter-spacing:2px;color:#1e1e1e}
.social{left:760px;top:35px;display:flex;gap:7px}
.social span{width:28px;height:28px;border-radius:50%;background:#8f8f8f;display:block}
.nav{left:99px;top:85px;display:flex;font-family:'Open Sans',sans-serif;font-size:12.5px;height:31px;align-items:center}
.nav a{color:#222;text-decoration:none;padding:0 20px;line-height:31px}
.nav a.active{background:linear-gradient(#d8b560,#b8933f);color:#fff;padding:0 13px}
.nav a.active+a{padding-left:24px}
.band{left:0;top:121px;width:1032px;height:6px;background:var(--gold-light)}
.main{left:104px;top:144px;width:823px;height:1007px;background:#fff;box-shadow:0 0 3px rgba(0,0,0,.2)}
.slide{left:117px;top:157px;width:538px;height:309px;background:linear-gradient(160deg,#f4f1ec 0%,#e9e3da 35%,#c77a5e 55%,#7a8f4a 80%,#e2dccf 100%)}
.slide-cap{left:117px;top:393px;width:538px;height:73px;background:rgba(90,90,90,.72)}
.slide-cap h2{position:absolute;left:105px;top:6px;font-family:'Cinzel',serif;font-weight:400;font-size:33px;color:#fff;letter-spacing:1px}
.slide-cap p{position:absolute;left:105px;top:47px;font-size:13px;color:#fff}
.dots{position:absolute;left:12px;top:32px;display:flex;gap:6px}
.dots i{width:12px;height:12px;border-radius:50%;background:#222;display:block}
.dots i:first-child{background:#e8dcc8}
.welcome{left:667px;top:157px;width:249px;height:307px;border-radius:14px;background:linear-gradient(#e7c565,#c9a655 60%,#b8964a)}
.welcome h3{position:absolute;left:8px;top:12px;font-family:'Cinzel',serif;font-weight:400;font-size:21px;color:#fff;letter-spacing:.5px;width:236px;border-bottom:1px dotted rgba(255,255,255,.6);padding-bottom:4px}
.welcome .portrait{position:absolute;left:8px;top:51px;width:233px;height:101px;background:#fff;padding:6px}
.welcome .portrait div{width:100%;height:100%;background:linear-gradient(90deg,#2c4fc2,#6e8de0 40%,#c49a83 60%,#3d6fd8)}
.welcome .quote{position:absolute;left:10px;top:163px;width:234px;font-family:'Open Sans',sans-serif;font-weight:300;font-size:19px;line-height:21px;color:#fff}
.welcome .bio{position:absolute;left:12px;top:213px;width:226px;font-size:12px;line-height:16px;color:#fff;text-align:justify}
.welcome .read{position:absolute;left:159px;top:270px;width:70px;height:21px;border:1px solid #f2dfa6;background:linear-gradient(#d7b662,#b8943f);color:#fff;font-size:10px;font-style:italic;font-weight:bold;text-align:center;line-height:19px}
.tile{top:494px;height:201px}
.tile .ph{width:100%;height:100%}
.tile .lbl{position:absolute;left:0;bottom:0;width:100%;height:38px;background:rgba(230,215,160,.55);font-family:'Open Sans',sans-serif;font-size:21px;color:#222;padding:4px 0 0 11px}
.tile.t2 .lbl{color:#fff}
.video{left:667px;top:494px;width:241px;height:201px;background:#a9a9a9;padding:8px}
.video .ph{width:100%;height:100%;background:linear-gradient(90deg,#e8e6e2,#cfc9c2 50%,#f0eee9)}
.video .bar{position:absolute;left:8px;bottom:8px;width:225px;height:14px;background:#eee;border-top:1px solid #ccc}
.sec-h{height:33px;font-family:'Cinzel',serif;font-size:19px;color:#fff;padding:5px 0 0 7px;letter-spacing:1px}
.sec-box{border:1px solid #ddd;background:var(--panel)}
.thumb{position:absolute;width:175px;height:120px}
.blurb{position:absolute;width:176px;font-family:'Cinzel',serif;font-size:11.5px;line-height:15.5px;color:var(--muted);letter-spacing:.5px}
.more{position:absolute;width:66px;height:19px;border-radius:3px;background:#2b2b2b;color:#fff;font-family:'Cinzel',serif;font-size:12px;padding-left:7px;line-height:19px;letter-spacing:1px}
.tweets{left:122px;top:972px;width:381px;height:140px;background:var(--tweet-bg);border:1px solid #e6dfb8;border-radius:6px}
.tweets h4{position:absolute;left:40px;top:7px;font-family:'Cinzel',serif;font-weight:400;font-size:17px;letter-spacing:1px}
.tweets .rule{position:absolute;left:108px;top:18px;width:265px;height:2px;background:var(--gold)}
.tweets .text{position:absolute;left:8px;top:37px;width:364px;font-size:10.5px;line-height:15.5px;text-align:justify}
.tweets em{color:var(--gold-dark);font-weight:bold}
.news{left:526px;top:972px;width:381px;height:140px;background:var(--panel);border:1px solid #ddd;border-radius:6px}
.news h4{position:absolute;left:14px;top:12px;font-family:'Cinzel',serif;font-weight:400;font-size:17px;letter-spacing:.5px}
.news .field{position:absolute;left:13px;top:41px;width:235px;height:29px;background:#fff;border:1px solid #ddd}
.news .sub{position:absolute;left:248px;top:41px;width:90px;height:29px;background:var(--gold-dark);color:#fff;font-family:'Cinzel',serif;font-size:14px;text-align:center;line-height:29px;letter-spacing:.5px}
.news .reg{position:absolute;left:14px;top:95px;width:230px;font-family:'Cinzel',serif;font-size:17px;line-height:19px;letter-spacing:.5px}
.news .click{position:absolute;left:247px;top:92px;width:91px;height:32px;border-radius:5px;background:linear-gradient(#444,#111);color:#fff;font-family:'Cinzel',serif;font-size:14px;text-align:center;line-height:32px;letter-spacing:.5px}
.footer{top:1173px;font-size:12px;color:#222}
</style>
</head>
<body>
<div class="abs header"></div>
<div class="abs brand">Renata Ossler RD</div>
<div class="abs social" aria-label="Social links"><span></span><span></span><span></span><span></span><span></span></div>
<nav class="abs nav">
  <a class="active">Home</a><a>About</a><a>Registered Dietitian</a><a>Healthy Recipes</a><a>Philanthropy</a><a>Shop</a><a>Features</a><a>Contact</a><a>Blog</a>
</nav>
<div class="abs band"></div>
<div class="abs main"></div>

<div class="abs slide" role="img" aria-label="Plated dish of cured ham wrapped around vegetables on greens"></div>
<div class="abs slide-cap">
  <div class="dots"><i></i><i></i><i></i></div>
  <h2>New Nutrition</h2>
  <p>simply dummy text of the printing the leap into electronic typesetting.</p>
</div>

<div class="abs welcome">
  <h3>Welcome to my Site</h3>
  <div class="portrait"><div role="img" aria-label="Portrait photo of the dietitian by the sea"></div></div>
  <div class="quote">Did not win. We bow to the region We bow to the earth</div>
  <div class="bio">The leap into electronic typesetting, remaining essentially unchanged. It was popularised in the 1960s</div>
  <div class="read">Read More</div>
</div>

<div class="abs tile" style="left:119px;width:253px">
  <div class="ph" role="img" aria-label="Hands preparing vegetables on a checked cloth" style="background:linear-gradient(160deg,#7d6a55,#a59a8a 45%,#6f8a5a 70%,#c9b38c)"></div>
  <div class="lbl">Food Philosophy</div>
</div>
<div class="abs tile t2" style="left:396px;width:254px">
  <div class="ph" role="img" aria-label="Pile of colourful fresh fruit and vegetables" style="background:linear-gradient(135deg,#c8342a,#7fa03a 35%,#6b3a6e 60%,#d24a2e 85%,#e8c04a)"></div>
  <div class="lbl">Food Philosophy</div>
</div>
<div class="abs video">
  <div class="ph" role="img" aria-label="Video still of the dietitian in a kitchen"></div>
  <svg class="abs" style="left:84px;top:55px" width="72" height="52" viewBox="0 0 72 52"><rect width="72" height="52" rx="6" fill="rgba(40,40,40,.75)"/><path d="M28 14 L50 26 L28 38Z" fill="#fff"/></svg>
  <div class="bar"></div>
</div>

<div class="abs sec-h" style="left:114px;top:728px;width:387px;background:var(--grey-band)">Recent Post</div>
<div class="abs sec-box" style="left:114px;top:761px;width:387px;height:170px"></div>
<div class="thumb" style="left:124px;top:782px;background:linear-gradient(135deg,#5a3a2e,#8a6a5e 50%,#4a2e24)" role="img" aria-label="Chocolate cupcakes dusted with heart shapes"></div>
<div class="abs" style="left:130px;top:876px;font-family:'Open Sans',sans-serif;font-size:17px;color:#fff">Chocolate Cupcakes</div>
<div class="blurb" style="left:310px;top:779px">Simply dummy text of the printing and typesetting industry. Lorem Ipsum has been the industry's standard dummy text ever since the 1500s.</div>
<div class="more" style="left:309px;top:880px">More..</div>

<div class="abs sec-h" style="left:520px;top:728px;width:387px;background:var(--gold)">Recent Recipes</div>
<div class="abs sec-box" style="left:520px;top:761px;width:387px;height:170px"></div>
<div class="thumb" style="left:527px;top:781px;background:linear-gradient(160deg,#f2f2f2,#e6a3a8 45%,#6b4a3c 75%,#f4f4f4)" role="img" aria-label="Cupcakes with pink frosting"></div>
<div class="blurb" style="left:717px;top:779px">Simply dummy text of the printing and typesetting industry. Lorem Ipsum has been the industry's standard dummy text ever since the 1500s.</div>
<div class="more" style="left:718px;top:880px">More..</div>

<div class="abs tweets">
  <svg class="abs" style="left:12px;top:7px" width="24" height="20" viewBox="0 0 24 20"><path d="M2 12 Q6 4 14 6 L22 3 L18 8 Q16 16 6 17 Q10 14 9 13 Q4 14 2 12Z" fill="var(--gold)"/></svg>
  <h4>Tweets</h4>
  <div class="rule"></div>
  <div class="text">Teaching @PKessane to cook @morningdesk at 8:45am....watch if u can!!<br><em>about 7 hours ago</em><br>Merci Beaucoup @ovanleck "@harlowtemming: @Mirabethl: @TVellamonte @harlowtemming thanku we had the best time! http://sh.example/bQx4Tn2R" <em>about 7 hours ago</em><br>Only the best for ur bday! "@Mirabethl: dinner at Le Corvanne: purse</div>
</div>

<div class="abs news">
  <h4>Join Renata Newsletter</h4>
  <div class="field"></div>
  <div class="sub">Subscribe</div>
  <div class="reg">Register For a Cooking Class</div>
  <div class="click">Click Here</div>
</div>

<div class="abs footer" style="left:107px">Copyright 2013 Renata Ossler (ACN 318 604 227).</div>
<div class="abs footer" style="left:745px">Privacy Policy | Terms &amp; Conditions</div>
</body>
</html>
```